Employee Portal UI Design - Modern and Clean

We are an agency tasked with developing a team portal for a company that has many employees. As we embark on this project, we seek a great UI design to accompany the requirements our client has for this project. We already have several screens mocked up that can be used as reference for the overall idea. Currently, we are only looking for the main dashboard's home page, user registration screen, and account settings page to be designed. The main brand colors are red but other accents can be used as well. The client's vision is for modern & minimalist to be at the center. We have a specific font to be used, but if you don't have access to it, you can just use a similar font.Main color: #DD0031The sub menus (do not need to be designed) would be:>Performance Reviews>Posts>Team directory>Calendar>Tasks>Documents>LinksWe would prefer the design be made in Adobe XD.

Industry/Entity Type

Fast Food Restaurant

Number of Pages Required

1 page

Font styles to use
Sans Serif

Colors
ec1f27

Requirements
Must have
• Color: #DD0031 (highlights)

```html
<!DOCTYPE html>
<html lang="en">
<head>
<meta charset="utf-8">
<title>Register</title>
<link href="https://fonts.googleapis.com/css2?family=Open+Sans:wght@300;400&display=swap" rel="stylesheet">
<style>
:root{
  --page:#ffffff;
  --band:#cccccc;
  --card:#ffffff;
  --card-border:#b8b8b8;
  --field-border:#dcdcdc;
  --text:#333333;
  --icon:#8f8f8f;
  --accent:#cc0033;
  --divider:#c4c4c4;
}
*{box-sizing:border-box;margin:0;padding:0}
html,body{width:1200px;height:1000px;overflow:hidden;background:var(--page);font-family:"Open Sans",sans-serif;color:var(--text)}
.band{position:absolute;left:0;top:125px;width:1200px;height:750px;background:var(--band)}
.title{position:absolute;top:170px;left:0;width:1200px;text-align:center;font-weight:300;font-size:35px;line-height:44px;color:#2e2e2e}
.card{position:absolute;left:149px;top:213px;width:902px;height:583px;background:var(--card);border:1px solid var(--card-border);border-radius:3px}
.column{position:absolute;top:21px;width:392px}
.column.left{left:29px}
.column.right{left:478px}
.divider{position:absolute;left:449px;top:21px;width:1px;height:424px;background:var(--divider)}
.field{height:81px}
.field label{display:block;font-size:14px;font-weight:300;line-height:18px;height:30px;padding-top:6px;color:#2b2b2b}
.input{position:relative;height:42px;border:1px solid var(--field-border);border-radius:4px;background:#fff}
.input svg{position:absolute;right:13px;top:12px;width:16px;height:16px;fill:var(--icon)}
.terms{position:absolute;top:461px;left:0;width:100%;text-align:center;font-size:14px;font-weight:300;line-height:20px}
a{color:var(--accent);text-decoration:underline;text-underline-offset:2px}
.register-btn{position:absolute;left:350px;top:501px;width:200px;height:50px;border:none;border-radius:3px;background:var(--accent);color:#fff;font-family:inherit;font-weight:300;font-size:21px}
.signin{position:absolute;top:801px;left:0;width:1200px;text-align:center;font-size:14px;font-weight:300;line-height:20px}
</style>
</head>
<body>
<svg width="0" height="0" style="position:absolute">
  <defs>
    <symbol id="i-user" viewBox="0 0 16 16"><circle cx="8" cy="4.5" r="3.3"/><path d="M2.5 15v-2.5C2.5 10 4.5 8.8 8 8.8s5.5 1.2 5.5 3.7V15z"/></symbol>
    <symbol id="i-mail" viewBox="0 0 16 16"><path d="M0 3h16v1.2L8 9 0 4.2z"/><path d="M0 5.8l8 4.8 8-4.8V13H0z"/></symbol>
    <symbol id="i-lock" viewBox="0 0 16 16"><path d="M4.5 7V5a3.5 3.5 0 0 1 7 0v2h-1.8V5a1.7 1.7 0 0 0-3.4 0v2z"/><rect x="2.5" y="7" width="11" height="8.5" rx="1.5"/></symbol>
    <symbol id="i-phone" viewBox="0 0 16 16"><path d="M3.2 0.8l2.3 2.9-1.3 2.1c.9 2.2 3.8 5.1 6 6l2.1-1.3 2.9 2.3-1.2 2.6C9 15.6.6 7 0.6 2z"/></symbol>
    <symbol id="i-pin" viewBox="0 0 16 16"><path d="M8 0.5a5.3 5.3 0 0 0-5.3 5.3C2.7 10 8 15.5 8 15.5s5.3-5.5 5.3-9.7A5.3 5.3 0 0 0 8 .5zm0 7.3a2.1 2.1 0 1 1 0-4.2 2.1 2.1 0 0 1 0 4.2z"/></symbol>
  </defs>
</svg>

<div class="band"></div>
<h1 class="title">Register</h1>

<form class="card">
  <div class="column left">
    <div class="field"><label>First Name</label><div class="input"><svg><use href="#i-user"/></svg></div></div>
    <div class="field"><label>Last Name</label><div class="input"><svg><use href="#i-user"/></svg></div></div>
    <div class="field"><label>Email</label><div class="input"><svg><use href="#i-mail"/></svg></div></div>
    <div class="field"><label>Password</label><div class="input"><svg><use href="#i-lock"/></svg></div></div>
    <div class="field"><label>Confirm Password</label><div class="input"><svg><use href="#i-lock"/></svg></div></div>
  </div>
  <div class="divider"></div>
  <div class="column right">
    <div class="field"><label>Phone</label><div class="input"><svg><use href="#i-phone"/></svg></div></div>
    <div class="field"><label>Address</label><div class="input"><svg><use href="#i-pin"/></svg></div></div>
    <div class="field"><label>City</label><div class="input"><svg><use href="#i-pin"/></svg></div></div>
    <div class="field"><label>State</label><div class="input"><svg><use href="#i-pin"/></svg></div></div>
    <div class="field"><label>Zip Code</label><div class="input"><svg><use href="#i-pin"/></svg></div></div>
  </div>
  <p class="terms">By clicking register you agree to our <a href="#">Terms and Conditions.</a></p>
  <button type="button" class="register-btn">Register</button>
</form>

<p class="signin">Already a user? <a href="#">Sign in.</a></p>
</body>
</html>
```